American cannabis tech company business card design

Thrum.com is seeking a modern, professional, and brand-aligned business card that represents our company and its core values: Mission, Story, Values, and Impact. As an innovative cannabis company, we want a business card that is not only visually appealing but also serves as a representation of who we are and what we stand for.

Project Scope: Design a double-sided business card that integrates our brand identity and core values. Incorporate our key brand elements, ensuring a sleek and contemporary aesthetic. Visually reflect our core values (Mission, Story, Values, Impact) in a way that is engaging yet professional.

Target Market(s)

Vendors, third parties,

Contact Information for Business Card

Contact details (name, title, email, phone, website, etc.)

Font styles to use
Other font styles liked:
• Caslon, Centra

Colors

Designer to choose colors to be used in the design.

Requirements
Must have
• Thrum.com logo and branding A creative yet clean way to integrate our core values (Mission, Story, Values, Impact) Modern typography and a well-structured layout
Nice to have
• forest green, grey, white, black
Should not have
• references to marijuana, leafs, plants, or related product

```html
<!DOCTYPE html>
<html lang="en">
<head>
<meta charset="utf-8">
<title>Thrum.com Business Card</title>
<link href="https://fonts.googleapis.com/css2?family=Arimo:wght@400;700&display=swap" rel="stylesheet">
<style>
  :root {
    --forest: #17351b;
    --paper: #ffffff;
    --swoosh: #a7a8ad;
    --stage: #e9ebe8;
    --ink-light: #ffffff;
    --ink-soft: #cfd6cf;
  }
  * { box-sizing: border-box; margin: 0; padding: 0; }
  html, body { width: 1200px; height: 874px; overflow: hidden; }
  body {
    background: var(--stage);
    font-family: "Arimo", Arial, sans-serif;
    position: relative;
  }
  .card {
    position: absolute;
    left: 320px;
    width: 560px;
    height: 320px;
    border-radius: 18px;
    overflow: hidden;
    box-shadow: 0 6px 18px rgba(0,0,0,0.18);
  }
  .card-front { top: 62px; background: var(--forest); }
  .card-back { top: 472px; background: var(--forest); }

  .front-stack {
    position: absolute;
    inset: 0;
    display: flex;
    flex-direction: column;
    align-items: center;
    justify-content: center;
    gap: 14px;
  }
  .front-wordmark {
    color: var(--ink-light);
    font-weight: 700;
    font-size: 100px;
    line-height: 1;
    letter-spacing: 2px;
  }
  .core-values {
    display: flex;
    gap: 14px;
    color: var(--ink-soft);
    font-size: 14px;
    letter-spacing: 3px;
    text-transform: uppercase;
  }
  .core-values span + span::before {
    content: "";
    display: inline-block;
    width: 4px;
    height: 4px;
    border-radius: 50%;
    background: var(--swoosh);
    margin: 0 14px 3px 0;
  }
  .back-art { position: absolute; inset: 0; width: 100%; height: 100%; }
  .back-wordmark {
    position: absolute;
    left: 34px;
    top: 38px;
    color: var(--forest);
    font-weight: 700;
    font-size: 62px;
    line-height: 1;
    letter-spacing: 1px;
  }
  .contact {
    position: absolute;
    right: 26px;
    bottom: 20px;
    text-align: right;
    color: var(--ink-light);
  }
  .contact-name { font-weight: 700; font-size: 20px; line-height: 24px; }
  .contact-title { font-size: 12px; margin: 0 21px 10px 0; }
  .contact-line {
    display: flex;
    justify-content: flex-end;
    align-items: center;
    gap: 8px;
    font-size: 14px;
    line-height: 21px;
  }
  .contact-line svg { width: 13px; height: 13px; flex: none; }
</style>
</head>
<body>
  <section class="card card-front" aria-label="Card front">
    <div class="front-stack">
      <div class="front-wordmark">THRUM</div>
      <div class="core-values">
        <span>Mission</span><span>Story</span><span>Values</span><span>Impact</span>
      </div>
    </div>
  </section>

  <section class="card card-back" aria-label="Card back">
    <svg class="back-art" viewBox="0 0 560 320" preserveAspectRatio="none" aria-hidden="true">
      <path d="M0,0 L518,0 C496,180 382,266 0,266 Z" fill="var(--swoosh)"/>
      <path d="M0,0 L490,0 C470,170 360,255 0,258 Z" fill="var(--paper)"/>
    </svg>
    <div class="back-wordmark">THRUM</div>
    <div class="contact">
      <div class="contact-name">Jordan Hale</div>
      <div class="contact-title">President</div>
      <div class="contact-line">+1 405-555-0148
        <svg viewBox="0 0 24 24"><path fill="#fff" d="M6.6 10.8a15 15 0 0 0 6.6 6.6l2.2-2.2a1 1 0 0 1 1-.25 11.4 11.4 0 0 0 3.6.57 1 1 0 0 1 1 1V20a1 1 0 0 1-1 1A17 17 0 0 1 3 4a1 1 0 0 1 1-1h3.5a1 1 0 0 1 1 1c0 1.25.2 2.45.57 3.57a1 1 0 0 1-.25 1z"/></svg>
      </div>
      <div class="contact-line">team@thrum.com
        <svg viewBox="0 0 24 24"><rect x="2" y="5" width="20" height="14" rx="1" fill="#fff"/><path d="M2 6l10 7 10-7" fill="none" stroke="var(--forest)" stroke-width="2"/></svg>
      </div>
      <div class="contact-line">www.Thrum.com
        <svg viewBox="0 0 24 24"><circle cx="12" cy="12" r="10" fill="#fff"/><path d="M2 12h20M12 2c3 3 3 17 0 20M12 2c-3 3-3 17 0 20" fill="none" stroke="var(--forest)" stroke-width="1.6"/></svg>
      </div>
    </div>
  </section>
</body>
</html>
```